Harvest Gathering event flyer

I would like a church event flyer designed. The event is called "HARVEST GATHERING 2018". I am looking for a professional, yet catchy design that uses our brand colors and logo creatively while communicating key information of the event effectively.

1. The logo is attached in two color formats. The designer has the choice to use them as he/she want.

2. The location of the event is: Lindqvist Community Center, 482 Tamsworth Street, Portland, ME 04102
3. Time and date of event. The designer can organize and format the date and time as he/she pleases.
December 28th, 29th @ 7:00PM
December 30th @ 10:00AM
4. The topic of the event is "Tongues of fire". The designer is free to use this phrase as he/she pleases to create a good composition.
5. Speaker: Prophet Marcus Obuya
6. Contact information: contact@cedarbrookfellowship.org - Telephone number: 207 555 0148

7. I would also like the following three words on the flyer. These words describe the focus of the event: FIRE, REVIVAL, PROPHETIC

```html
<!DOCTYPE html>
<html lang="en">
<head>
<meta charset="utf-8">
<title>Harvest Gathering 2018 – Tongues of Fire</title>
<link rel="stylesheet" href="https://fonts.googleapis.com/css2?family=Bebas+Neue&family=Cinzel:wght@500&family=Poppins:wght@200;300&family=Open+Sans:wght@400;700;800&family=Sedgwick+Ave+Display&family=Allura&family=Raleway:wght@200;300&display=swap">
<style>
  :root {
    --orange: #e9952f;
    --orange-deep: #e07a20;
    --amber: #d68a2a;
    --navy: #0a0a3c;
    --brand-navy: #0e3a5a;
    --white: #ffffff;
    --black: #000000;
  }
  html, body { margin: 0; padding: 0; overflow: hidden; }
  .flyer {
    position: relative;
    width: 928px;
    height: 1200px;
    background: var(--white);
    overflow: hidden;
    font-family: "Open Sans", sans-serif;
  }
  .flyer > * { position: absolute; margin: 0; }

  .event-series {
    left: 70px; top: 102px;
    font-family: "Bebas Neue", sans-serif;
    font-size: 54px; line-height: 0.96;
    color: var(--orange);
  }
  .brand-name {
    left: 339px; top: 138px; width: 262px;
    text-align: center;
    font-family: "Cinzel", serif; font-weight: 500;
    font-size: 62px; line-height: 1;
    color: var(--brand-navy);
  }
  .presents {
    left: 380px; top: 206px; width: 200px;
    text-align: center;
    font-family: "Poppins", sans-serif; font-weight: 200;
    font-size: 52px; line-height: 1;
    color: var(--navy);
  }
  .event-title {
    left: 0; top: 268px; width: 928px;
    text-align: center;
    font-family: "Open Sans", sans-serif; font-weight: 700;
    font-size: 108px; line-height: 0.92;
    color: var(--orange);
  }
  .focus-band {
    left: 0; top: 466px; width: 928px; height: 64px;
    background: var(--navy);
  }
  .focus-words {
    left: 0; top: 476px; width: 928px;
    text-align: center;
    font-family: "Raleway", sans-serif; font-weight: 200;
    font-size: 34px; letter-spacing: 3px; line-height: 44px;
    color: var(--white);
  }
  .invite {
    left: 0; top: 548px; width: 928px;
    text-align: center;
    font-family: "Sedgwick Ave Display", cursive;
    font-size: 104px; line-height: 1;
    color: var(--navy);
  }
  .schedule {
    left: 136px; top: 664px; width: 690px;
    display: flex; justify-content: space-between;
  }
  .session { display: flex; flex-direction: column; align-items: center; }
  .session-date {
    font-weight: 700; font-size: 25px; letter-spacing: 1.5px;
    color: var(--orange); line-height: 30px; white-space: nowrap;
  }
  .session-date sup { font-size: 14px; }
  .session-time {
    margin-top: 4px; width: 176px; height: 30px; border-radius: 15px;
    background: var(--navy); color: var(--white);
    font-family: "Raleway", sans-serif; font-weight: 200;
    font-size: 30px; line-height: 30px; text-align: center;
  }
  .tagline {
    left: 0; top: 760px; width: 958px;
    text-align: center; font-size: 29px; line-height: 34px;
    color: var(--orange);
  }
  .tagline-script {
    left: 0; top: 790px; width: 948px;
    text-align: center;
    font-family: "Allura", cursive;
    font-size: 82px; line-height: 1;
    color: var(--orange);
  }
  .speaker-label {
    left: 0; top: 876px; width: 948px;
    text-align: center; font-weight: 800; font-size: 26px; letter-spacing: 1px;
    color: var(--amber);
  }
  .speaker-name {
    left: 274px; top: 918px; width: 424px; height: 42px; border-radius: 12px;
    background: var(--black); color: var(--white);
    font-family: "Raleway", sans-serif; font-weight: 300;
    font-size: 29px; letter-spacing: 1.5px; line-height: 42px; text-align: center;
  }
  .location-label {
    left: 0; top: 992px; width: 948px;
    text-align: center; font-weight: 700; font-size: 38px; letter-spacing: 1.5px;
    color: var(--orange-deep);
  }
  .venue {
    left: 0; top: 1032px; width: 948px;
    text-align: center; font-family: "Raleway", sans-serif; font-weight: 300;
    font-size: 28px; letter-spacing: 1px; color: var(--navy);
  }
  .venue strong { font-family: "Open Sans", sans-serif; font-weight: 700; }
  .address {
    left: 0; top: 1080px; width: 948px;
    text-align: center; font-family: "Raleway", sans-serif; font-weight: 300;
    font-size: 27px; letter-spacing: 1px; color: var(--navy);
  }
  .contact-pill {
    left: 0; top: 1130px; width: 254px; height: 38px; border-radius: 0 19px 19px 0;
    background: var(--orange-deep); color: var(--white);
    font-family: "Poppins", sans-serif; font-weight: 300;
    font-size: 17px; line-height: 38px; text-align: right; padding-right: 10px; box-sizing: border-box;
  }
  .contact-email, .contact-phone {
    top: 1138px; font-family: "Poppins", sans-serif; font-weight: 300;
    font-size: 14px; line-height: 22px; color: var(--black); letter-spacing: 0.4px;
  }
  .contact-email { left: 268px; }
  .contact-divider { left: 598px; top: 1128px; width: 1.5px; height: 42px; background: var(--black); }
  .contact-phone { left: 612px; }
</style>
</head>
<body>
<main class="flyer">
  <h2 class="event-series">Harvest<br>Gathering<br>2018</h2>
  <p class="brand-name">KESTREL</p>
  <p class="presents">presents</p>
  <h1 class="event-title">TONGUES<br>OF FIRE</h1>

  <div class="focus-band"></div>
  <p class="focus-words">FIRE. REVIVAL. PROPHETIC.</p>

  <p class="invite">YOU'RE INVITED!</p>

  <div class="schedule">
    <div class="session"><span class="session-date">DECEMBER 28<sup>TH</sup></span><span class="session-time">7:00 PM</span></div>
    <div class="session"><span class="session-date">DECEMBER 29<sup>TH</sup></span><span class="session-time">7:00 PM</span></div>
    <div class="session"><span class="session-date">DECEMBER 30<sup>TH</sup></span><span class="session-time">10:00 AM</span></div>
  </div>

  <p class="tagline">SET YOUR SOUL ON FIRE WITH CHRIST....</p>
  <p class="tagline-script">Here at the revival</p>

  <p class="speaker-label">WITH SPEAKER,</p>
  <p class="speaker-name">PROPHET MARCUS OBUYA</p>

  <p class="location-label">LOCATION:</p>
  <p class="venue">LINDQVIST <strong>COMMUNITY</strong> CENTER</p>
  <p class="address">482 Tamsworth Street, Portland, ME 04102</p>

  <p class="contact-pill">For More Information</p>
  <p class="contact-email">Email : contact@cedarbrookfellowship.org</p>
  <div class="contact-divider"></div>
  <p class="contact-phone">CALL : 207 555 0148</p>
</main>
</body>
</html>
```